Building company buisness cards

We are looking for a sharp modern new look for our business cards.
We are a New Zealand based company that specialises in house and land packages.
We have attached a photo of the current logo and would like to see if it can be improved somehow if needed.
We are open to any colours but we have chosen green at this stage.
Feel free to change the font and make the logo smarter looking.
Play with the colours and see what looks best.

We want a card that looks so good know one will want to throw it away!

Target Market(s)

Home buyers

Industry/Entity Type

Building

Contact Information for Business Card

Garth Ellery
0219364028
gellery@tidewaterhomecraft.co.nz
tidewaterhomecraft.co.nz

Font styles to use
Serif
Sans Serif

Colors

Designer to choose colors to be used in the design.

Requirements
Must have
• Logo and company name on one side, details on the other side
Nice to have
• Color codes for the original green are HEX #4a8028, RGB(74,128,40), CMYK(42,0,69,50)
• Round corners, Raised and/or spot UV

```html
<!DOCTYPE html>
<html lang="en">
<head>
<meta charset="utf-8">
<title>Tidewater Homecraft – Business Cards</title>
<link rel="stylesheet" href="https://fonts.googleapis.com/css2?family=Open+Sans:wght@400;700;800&family=Arimo:wght@700&display=swap">
<style>
  :root {
    --green: #4a8028;
    --green-tint: #e4eedd;
    --swoosh: #6b6b6b;
    --ink: #1f1f1f;
    --paper: #ffffff;
    --backdrop: #c8c9cb;
  }
  * { box-sizing: border-box; margin: 0; padding: 0; }
  html, body { width: 1200px; height: 1015px; overflow: hidden; }
  body {
    background: var(--backdrop);
    font-family: "Open Sans", sans-serif;
    position: relative;
  }
  .card {
    position: absolute;
    width: 686px;
    height: 393px;
    background: var(--paper);
    border-radius: 33px;
    overflow: hidden;
    box-shadow: 0 1px 4px rgba(0,0,0,0.35);
  }
  .card--front { left: 92px; top: 89px; border: 1px solid #555; }
  .card--back  { left: 416px; top: 536px; }

  .wordmark {
    position: absolute;
    color: var(--green);
    font-family: "Open Sans", sans-serif;
    font-weight: 800;
    line-height: 1;
    letter-spacing: -0.5px;
  }
  .wordmark__dot {
    display: inline-block;
    border-radius: 50%;
    background: var(--green);
  }
  .card--front .wordmark {
    left: 0; right: 0; top: 44px;
    display: flex; align-items: center; justify-content: center; gap: 14px;
  }
  .card--front .wordmark__dot { width: 44px; height: 44px; }
  .card--front .wordmark__text { font-size: 36px; }

  .holder {
    position: absolute; left: 0; right: 0; top: 158px;
    text-align: center;
    font-family: "Arimo", sans-serif;
    font-weight: 700; font-size: 26px;
    color: var(--green);
  }
  .phone {
    position: absolute; left: 0; right: 0; top: 222px;
    display: flex; justify-content: center; align-items: center; gap: 8px;
    font-weight: 700; font-size: 25px; letter-spacing: 0.5px;
    color: var(--green);
  }
  .phone svg { width: 22px; height: 22px; }
  .email {
    position: absolute; left: 0; right: 0; top: 262px;
    display: flex; justify-content: center; align-items: center; gap: 7px;
    font-size: 14.5px; color: var(--ink); letter-spacing: -0.2px;
  }
  .email svg { width: 17px; height: 13px; }
  .front-wave { position: absolute; left: 0; top: 0; width: 686px; height: 393px; }
  .site-band {
    position: absolute; left: 0; right: 0; top: 356px;
    text-align: center;
    color: var(--paper);
    font-size: 16px; letter-spacing: 2px;
  }

  .back-mark {
    position: absolute; left: 80px; top: 50px;
    width: 300px; height: 300px; border-radius: 50%;
    background: var(--green-tint);
  }
  .card--back .wordmark {
    left: 380px; width: 300px; top: 272px;
    text-align: center;
    font-size: 30px;
  }
  .rule {
    position: absolute; left: 464px; top: 343px;
    width: 109px; height: 1px; background: var(--green);
  }
  .back-site {
    position: absolute; right: 14px; top: 356px;
    font-size: 17px; color: var(--ink);
  }
  .back-site span { color: var(--green); }
</style>
</head>
<body>

  <section class="card card--front">
    <svg class="front-wave" viewBox="0 0 686 393" aria-hidden="true">
      <path d="M0 257 C150 318 380 345 569 338 C380 352 150 332 0 272 Z" fill="var(--swoosh)"/>
      <path d="M0 281 C180 340 400 360 686 321 L686 393 L0 393 Z" fill="var(--green)"/>
    </svg>

    <div class="wordmark">
      <span class="wordmark__dot"></span>
      <span class="wordmark__text">tidewater homecraft.</span>
    </div>

    <h1 class="holder">Garth Ellery</h1>

    <p class="phone">
      <svg viewBox="0 0 24 24" aria-hidden="true">
        <circle cx="12" cy="12" r="10.5" fill="none" stroke="var(--green)" stroke-width="1.6"/>
        <path d="M9 6.5 C7 8 7 13 10 16 C12.5 18.5 15.5 18.5 17 17 L15.2 14.8 L13.5 15.5 C12 14.5 10 12 9.8 10.5 L11.2 9.2 Z" fill="var(--green)"/>
      </svg>
      0219364028
    </p>

    <p class="email">
      <svg viewBox="0 0 17 13" aria-hidden="true">
        <path d="M0 5 L8.5 0 L17 5 L17 13 L0 13 Z" fill="var(--green)"/>
        <path d="M2 5 L8.5 9 L15 5" fill="none" stroke="#fff" stroke-width="1.4"/>
      </svg>
      gellery@tidewaterhomecraft.co.nz
    </p>

    <p class="site-band">www.tidewaterhomecraft.co.nz</p>
  </section>

  <section class="card card--back">
    <div class="back-mark"></div>
    <div class="wordmark">tidewater<br>homecraft.</div>
    <div class="rule"></div>
    <p class="back-site">www.<span>tidewaterhomecraft</span>.co.nz</p>
  </section>

</body>
</html>
```